Audit/Compliance company needs Business Card Template

We are after a Business Card Template that we can modify internally to update details as people change positions.
We are an Australian based company specalising in Auditing and Quality/OHS systems development. - See www.kelvaranorth.com.au for more information
We would like the desings to be based around our logo and colours assocaited with it (attached for your information) however we are very open as to how the cards are designed.
We are looking for something quite edgy and mordern but it must have a professional/compliance feel to it (if possible).
The main details we would like to include within the card template are:
Name
Position Title
Postal Address
Phone Number
Mobile Number
Email Address
Website
The cards will be printed through tally press on Glossy paper so it should reflect the requirements below
Full Bleed Size (starting document size)
90 x 52 mm
1062 x 615 pixels
Document Trim Size (final size after being cut)
87 x 49 mm
1028 x 579 pixels
Resolution
300 DPI

```html
<!DOCTYPE html>
<html lang="en">
<head>
<meta charset="utf-8">
<title>Kelvara North Audit &amp; Compliance – Business Cards</title>
<link rel="stylesheet" href="https://fonts.googleapis.com/css2?family=Tinos&family=Questrial&family=Montserrat:wght@600&display=swap">
<style>
  :root {
    --backdrop: #e9e7e2;
    --card-dark: #242424;
    --card-light: #f7f7f6;
    --brand-orange: #f39a1d;
    --brand-blue: #1f5f8d;
    --label-blue: #2b74ad;
    --ink-light: #ffffff;
    --ink-dark: #4a4a4a;
    --ink-muted: #6b6b6b;
    --divider-dark: #8a8a8a;
    --divider-light: #9a9a9a;
  }
  * { margin: 0; padding: 0; box-sizing: border-box; }
  html, body { width: 1200px; height: 800px; overflow: hidden; }
  body { background: var(--backdrop); position: relative; }

  .card {
    position: absolute;
    box-shadow: 0 6px 18px rgba(0, 0, 0, 0.25);
  }
  .card--front {
    left: 170px; top: 280px; width: 557px; height: 280px;
    background: var(--card-dark);
  }
  .card--back {
    left: 468px; top: 462px; width: 605px; height: 248px;
    background: var(--card-light);
  }

  .brand {
    position: absolute;
    display: flex;
    align-items: center;
  }
  .brand__mark {
    background: var(--brand-orange);
    flex: none;
  }
  .brand__rule { flex: none; }
  .brand__name {
    font-family: "Tinos", "Times New Roman", serif;
    font-weight: 400;
    text-transform: uppercase;
    line-height: 1.1;
  }
  .brand__name span { display: block; }

  .card--front .brand { left: 52px; top: 88px; }
  .card--front .brand__mark { width: 86px; height: 86px; }
  .card--front .brand__rule {
    width: 1px; height: 62px; margin: 0 10px 0 56px;
    background: var(--divider-dark);
  }
  .card--front .brand__name {
    color: var(--ink-light);
    font-size: 20px;
    letter-spacing: 0.5px;
  }

  .card--back .brand { left: 56px; top: 44px; }
  .card--back .brand__mark { width: 78px; height: 78px; }
  .card--back .brand__rule {
    width: 1px; height: 58px; margin: 0 10px 0 54px;
    background: var(--divider-light);
  }
  .card--back .brand__name {
    color: var(--ink-dark);
    font-size: 18px;
    letter-spacing: 0.5px;
  }

  .person {
    position: absolute;
    left: 132px; top: 160px;
    text-align: right;
    width: 136px;
  }
  .person__name {
    font-family: "Montserrat", Arial, sans-serif;
    font-weight: 600;
    font-size: 13px;
    letter-spacing: 0.5px;
    color: var(--ink-dark);
    text-transform: uppercase;
  }
  .person__role {
    font-family: "Questrial", Arial, sans-serif;
    font-size: 12px;
    color: var(--ink-muted);
  }

  .contact {
    position: absolute;
    left: 308px; top: 150px;
    font-family: "Questrial", Arial, sans-serif;
    font-size: 10.5px;
    line-height: 15px;
    color: var(--ink-muted);
    list-style: none;
  }
  .contact__label {
    color: var(--label-blue);
    font-weight: 700;
  }
</style>
</head>
<body>
  <section class="card card--front" aria-label="Business card front">
    <div class="brand">
      <div class="brand__mark"></div>
      <div class="brand__rule"></div>
      <p class="brand__name"><span>Kelvara North Audit</span><span>&amp; Compliance</span></p>
    </div>
  </section>

  <section class="card card--back" aria-label="Business card back">
    <div class="brand">
      <div class="brand__mark"></div>
      <div class="brand__rule"></div>
      <p class="brand__name"><span>Kelvara North Audit</span><span>&amp; Compliance</span></p>
    </div>

    <div class="person">
      <p class="person__name">Dana Whitlock</p>
      <p class="person__role">Manager</p>
    </div>

    <ul class="contact">
      <li>42 Corran Street, Hobart, TAS 7000</li>
      <li><span class="contact__label">M:</span> (03) 6120 4415 &middot; <span class="contact__label">T:</span> (03) 6120 4416</li>
      <li><span class="contact__label">E:</span> info@kelvaranorth.com.au</li>
      <li>www.kelvaranorth.com.au</li>
    </ul>
  </section>
</body>
</html>
```